Indonesian B2B Company (Varo Ingredients) - Stationery Design

Varo Ingredients needs a corporate, bold and professional-looking stationery design.

Varo Ingredients is a new Indonesian company manufacturing, marketing and distributing various ingredients / raw materials such as flavours, fragrance, colours, sweeteners, preservatives for the food & beverage, pharmaceutical, personal care and other household goods industries.

It is a business to business (B2B) company as we supply various natural and synthetic raw materials to various consumer goods manufacturers. We therefore need a logo/identity with corporate and industrial style.

Varo Ingredients is a startup company which belongs to a larger Tumina Jaya group of companies (http://tuminajaya.bizplank.example/about) that focuses in the mining, petroleum and energy businesses. Varo Ingredients would like to focus in providing good quality, safe, reliable and affordable ingredients for the industries. Our tagline is "Ingredients for Your Success"
Updates

We have updated some information including our requirements and contact details to be shown in the stationery. Please check the project brief.

Regards,

Varo Ingredients

Target Market(s)

Manufacturers of food & beverages, personal care, pharmaceutical and other FMCG factories.

Industry/Entity Type

Business

Requirements
Must have
• Smart, professional and corporate touches in the stationery designs. We require designs for:
1. Letterhead
2. Envelope (with and without window)
3. Name card
4. Powerpoint presentation template
5. CD label
6. Small memo / with compliments card

Contact details:

Company name:
PT Varo Ingredients

Address:
Ruko Pelita Sumber Asri, Blok K07 no: 15-16
Cempaka Hijau Utara, 14590
Indonesia

Tel:+62 21 738 2096
Fax:+62 21 738 2097
Email: info@varo-ingredients.example
Website: www.varo-ingredients.example

```html
<!DOCTYPE html>
<html lang="en">
<head>
<meta charset="utf-8">
<title>Varo Ingredients – Business Card</title>
<link rel="stylesheet" href="https://fonts.googleapis.com/css2?family=Alegreya+Sans:wght@400;500&family=Marcellus&display=swap">
<style>
  :root {
    --stage: #3b3b3b;
    --card-white: #ffffff;
    --brand-blue: #1e80cc;
    --brand-blue-deep: #1a72bd;
    --brand-blue-light: #3196de;
    --brand-red: #d3262c;
    --ink: #111111;
    --muted: #8a8a8a;
    --tagline-light: #c9dcef;
    --label-white: #ffffff;
  }
  * { margin: 0; padding: 0; box-sizing: border-box; }
  html, body { width: 1200px; height: 918px; overflow: hidden; }
  body {
    position: relative;
    background: var(--stage);
    font-family: "Alegreya Sans", sans-serif;
  }
  .card {
    position: absolute;
    width: 731px;
    height: 416px;
  }
  .card-front { left: 26px; top: 20px; background: var(--card-white); }
  .card-back {
    left: 431px; top: 457px;
    background: linear-gradient(120deg, var(--brand-blue-deep) 0%, var(--brand-blue-light) 55%, var(--brand-blue) 100%);
  }

  .holder { position: absolute; right: 451px; top: 150px; text-align: right; }
  .holder-name { font-size: 33px; color: var(--brand-blue); line-height: 1.1; font-weight: 400; }
  .holder-title { font-size: 21px; color: var(--ink); margin-top: 4px; }

  .brand { position: absolute; left: 36px; top: 304px; display: flex; align-items: center; gap: 14px; }
  .brand-mark { width: 40px; height: 40px; background: var(--brand-red); }
  .brand-name { font-size: 25px; color: var(--brand-red); font-weight: 500; line-height: 1; }
  .brand-tagline { font-size: 13px; color: var(--muted); margin-top: 4px; }

  .contact { position: absolute; left: 359px; top: 38px; font-size: 19px; line-height: 24px; color: var(--ink); }
  .contact-label { color: var(--brand-blue); }
  .contact-block + .contact-block { margin-top: 24px; }

  .accent-bar { position: absolute; left: 348px; top: 342px; width: 383px; height: 19px; background: var(--brand-blue); }

  .back-brand { position: absolute; left: 0; width: 331px; top: 316px; text-align: center; }
  .back-name { font-size: 35px; color: var(--card-white); font-weight: 500; line-height: 1; }
  .back-tagline { font-size: 18px; color: var(--tagline-light); margin-top: 6px; }

  .board-label {
    position: absolute; left: 785px; top: 240px;
    font-family: "Marcellus", serif; font-size: 50px; color: var(--label-white);
  }
</style>
</head>
<body>
  <section class="card card-front" aria-label="Business card front">
    <div class="holder">
      <p class="holder-name">Adrian Putra</p>
      <p class="holder-title">Post Title</p>
    </div>

    <div class="brand">
      <span class="brand-mark"></span>
      <div>
        <p class="brand-name">Varo Ingredients</p>
        <p class="brand-tagline">Ingredients for Your Success</p>
      </div>
    </div>

    <div class="contact">
      <div class="contact-block">
        <p class="contact-label">Address:</p>
        <p>Ruko Pelita Sumber Asri,<br>Blok K07 no: 15-16 Cempaka<br>Hijau Utara, 14590<br>Indonesia.</p>
      </div>
      <div class="contact-block">
        <p class="contact-label">Web/Email:</p>
        <p>info@varo-ingredients.example<br>www.varo-ingredients.example</p>
      </div>
      <div class="contact-block">
        <p class="contact-label">Phones:</p>
        <p>+62 21 738 2097, +62 21 738 2096</p>
      </div>
    </div>

    <div class="accent-bar"></div>
  </section>

  <section class="card card-back" aria-label="Business card back">
    <div class="back-brand">
      <p class="back-name">Varo Ingredients</p>
      <p class="back-tagline">Ingredients for Your Success</p>
    </div>
  </section>

  <p class="board-label">Business Card</p>
</body>
</html>
```